Flyer Design Project - Announcing New Dental Building

**UPDATE**
Here's the basics: Flyer for New Dental Building. Moving in August 2013. 2418 N Birch Avenue. Include Map.
Go.
****************

We need a flyer announcing our move to a new building in August 2013. We are a general dentistry practice that sees families and people of all ages in Centralia, WA (Small town between Seattle and Portand).

We would like to see designs that feature a fun/lively sketch of the new building. Could even be silhouette. Tall evergreen cedar/hemlock type trees in the back ground would also be appropriate (our logo has these in backgournd). Enticing. Simple.

I would prefer a more "artistic" "hand drawn" type look over flashy graphics - but I'm open to ideas.

The text can be simple, "We're moving! Visit us at our new location in August. 2418 North Birch Avenue" ... again, I"m open to some variation here.

I'd like this to be one flat page.

Our website is www.hollowbrooksmiles.example
Facebook: www.facebook.com/hollowbrooksmiles

(Although website is now about 3 years old)
Updates

Pictures of new building construction available on Facebook.com/hollowbrooksmiles

I'd like more of a fun sketch of building - versus the architectural rendering. Could even be silhouette.

Thank you!

Decided that flyer really should have map.  I'm attaching a map I've drawn from our current location (circle) to our new location (star). I like the map to be clean and simple.

Reason: I've not seen a fun, beautiful hand drawn design that looks like a good fit yet. It should include a map (see download). It does NOT need to have our logo.

Some major projects here - will get back soon to provide feedback.  Thank you everyone for your designs so far!

Target Market(s)

Women, existing patients of our dental practice. Families.

Industry/Entity Type

Building

Requirements
Must have
• **Map**See download for preferred directions (there are one way streets).

```html
<!DOCTYPE html>
<html lang="en">
<head>
<meta charset="utf-8">
<title>Hollowbrook Family Dental – We're Moving</title>
<link rel="stylesheet" href="https://fonts.googleapis.com/css2?family=Open+Sans:wght@300;400;700;800&display=swap">
<style>
  :root {
    --backdrop: #8a8a8a;
    --backdrop-light: #a3a3a3;
    --green-light: #24a07a;
    --green: #138563;
    --green-dark: #0b5f46;
    --lime: #d6e63a;
    --gold: #ffd21a;
    --red: #d7191f;
    --red-dark: #9e0f13;
    --paper: #ededed;
    --paper-shade: #cfcfcf;
    --sky: #7fb1e3;
    --sky-pale: #dfeaf5;
    --building: #b9b7b2;
    --white: #ffffff;
    --brand-green: #1c7a57;
  }
  * { margin: 0; padding: 0; box-sizing: border-box; }
  html, body { width: 1200px; height: 960px; overflow: hidden; }
  body {
    background: radial-gradient(ellipse at center, var(--backdrop-light) 0%, var(--backdrop) 75%);
    font-family: "Open Sans", Arial, sans-serif;
    position: relative;
  }
  .flyer {
    position: absolute;
    left: 300px; top: 25px;
    width: 600px; height: 910px;
    background: var(--paper);
    overflow: hidden;
    box-shadow: 0 12px 30px rgba(0,0,0,0.35);
  }
  .flyer-shapes { position: absolute; inset: 0; }
  .building-photo { position: absolute; left: 0; top: 0; width: 600px; height: 270px;
    background: linear-gradient(180deg, var(--sky) 0%, var(--sky-pale) 45%, var(--building) 70%, #8c8a84 100%); }
  .map-sketch { position: absolute; left: 40px; top: 470px; width: 360px; height: 230px;
    background: linear-gradient(180deg, #fafafa, #dcdcdc); border-radius: 4px;
    box-shadow: 0 4px 10px rgba(0,0,0,0.25); }
  .brand { position: absolute; top: 50px; left: 0; width: 600px; text-align: center;
    color: var(--brand-green); font-size: 40px; font-weight: 400; letter-spacing: -0.5px; }
  .headline { position: absolute; left: 60px; top: 290px; color: var(--white); }
  .headline-lead { font-size: 64px; font-weight: 300; line-height: 1; }
  .headline-key { font-size: 56px; font-weight: 800; color: var(--lime); line-height: 1.1; }
  .move-date { position: absolute; left: 400px; top: 290px; width: 200px; text-align: center; color: var(--white); line-height: 1.05; }
  .move-date-in { font-size: 44px; font-weight: 300; }
  .move-date-month { font-size: 38px; font-weight: 800; color: var(--gold); }
  .move-date-year { font-size: 46px; font-weight: 300; }
  .new-address { position: absolute; left: 424px; top: 480px; width: 148px; color: var(--white); }
  .new-address-name { font-size: 16px; line-height: 1.2; padding-bottom: 10px; border-bottom: 1px solid rgba(255,255,255,0.6); }
  .new-address-street { font-size: 23px; font-weight: 400; line-height: 1.25; margin-top: 12px; }
  .visit-note { position: absolute; left: 195px; top: 826px; color: var(--white); font-size: 21px; font-weight: 400;
    transform: rotate(-15deg); transform-origin: left top; white-space: nowrap; }
</style>
</head>
<body>
  <article class="flyer">
    <div class="building-photo" role="img" aria-label="Photograph of the new single-storey dental building under blue sky"></div>

    <svg class="flyer-shapes" width="600" height="910" viewBox="0 0 600 910" aria-hidden="true">
      <defs>
        <linearGradient id="ribbon" x1="0" y1="0" x2="0" y2="1">
          <stop offset="0" stop-color="var(--green-light)"/>
          <stop offset="1" stop-color="var(--green)"/>
        </linearGradient>
        <linearGradient id="tab" x1="0" y1="0" x2="0" y2="1">
          <stop offset="0" stop-color="var(--green)"/>
          <stop offset="1" stop-color="var(--green-dark)"/>
        </linearGradient>
        <linearGradient id="redbox" x1="0" y1="0" x2="0" y2="1">
          <stop offset="0" stop-color="var(--red)"/>
          <stop offset="1" stop-color="var(--red-dark)"/>
        </linearGradient>
        <linearGradient id="paperfade" x1="0" y1="0" x2="0" y2="1">
          <stop offset="0" stop-color="#f6f6f6"/>
          <stop offset="1" stop-color="var(--paper-shade)"/>
        </linearGradient>
      </defs>
      <rect x="0" y="430" width="600" height="480" fill="url(#paperfade)"/>
      <polygon class="ribbon-band" points="0,262 400,262 400,440 0,440" fill="url(#ribbon)"/>
      <polygon class="ribbon-fold" points="400,440 385,455 385,440" fill="var(--green-dark)"/>
      <polygon class="date-tab" points="385,282 600,268 600,440 385,455" fill="url(#tab)"/>
      <rect class="address-box" x="412" y="462" width="170" height="200" fill="url(#redbox)"/>
      <polygon class="footer-band" points="0,860 600,700 600,910 0,910" fill="url(#ribbon)"/>
      <polygon class="footer-shade" points="0,860 600,700 600,720 0,880" fill="var(--green-dark)" opacity="0.5"/>
    </svg>

    <div class="map-sketch" role="img" aria-label="Hand-drawn street map from the current office to the new location, with a magnifying glass over the new address"></div>

    <header class="brand">Hollowbrook Family Dental</header>

    <h1 class="headline">
      <span class="headline-lead">We’re</span><br>
      <span class="headline-key">MOVING</span>
    </h1>

    <div class="move-date">
      <div class="move-date-in">in</div>
      <div class="move-date-month">AUGUST</div>
      <div class="move-date-year">2013</div>
    </div>

    <div class="new-address">
      <div class="new-address-name">Hollowbrook Family Dental</div>
      <div class="new-address-street">2418 North Birch Avenue</div>
    </div>

    <p class="visit-note">Visit us at our new location in August</p>
  </article>
</body>
</html>
```